依頼詳細
封筒デザインを依頼します。封筒は相続人様にももちろん、各業者様に送る際にも使えるような万能型でお願いしたいと思います。

サイズの種類は①角2 窓なし、②長3 縦 窓なし、③長3 横 窓付きの3点で同じテイストで結構です。デザインは表面のみ、色はフルカラー、封筒の色は白を予定しています。

作成して頂いたデザインで最終的にモビタンにて発注予定のため、最終的にコンペにて選ばれた方には、下記のテンプレートの要領に従って入稿データの作成についてお願い致します。郵便番号枠は「なし」です。
https://mobitan-print.example/guide/how-to-make-data/envelope/

ロゴデータ、名刺データを添付いたします。
記載項目
表面:
・ロゴ
・事務所名
・郵便番号
・住所(建物・部屋番号まで)
・電話 (携帯電話番号不要)
FAXは利用していません。
希望イメージ
シンプル 複雑
単色 カラフル
暗い 明るい
日常 高級
遊び心 厳粛
未来的 伝統的
女性的 男性的
希望する色
青系、水色系

ご提案の文章にあるように「落ち着きのある中に気持ち先進感」なデザインが気に入りました。名刺デザインからさらに工夫を加えられており、イメージしてた以上に良いデザインをご提案いただきました。

みなさま、それぞれに素敵なデザインをご提案いただきましてありがとうございました。

```html
<!DOCTYPE html>
<html lang="ja">
<head>
<meta charset="utf-8">
<title>青葉台相続専門税理士事務所 封筒 角2</title>
<link href="https://fonts.googleapis.com/css2?family=Noto+Sans+JP:wght@400;500&display=swap" rel="stylesheet">
<style>
  :root {
    --paper: #ffffff;
    --fold-line: #e3e6ea;
    --ink: #1d2a44;
    --brand-blue: #1f4d9c;
    --brand-navy: #14357a;
    --band-light: #c9d6e8;
    --watermark: #e9eef6;
  }
  html, body {
    margin: 0;
    padding: 0;
    width: 849px;
    height: 1200px;
    overflow: hidden;
    background: var(--paper);
  }
  .envelope {
    position: relative;
    width: 849px;
    height: 1200px;
    background: var(--paper);
    font-family: "Noto Sans JP", sans-serif;
    color: var(--ink);
  }
  .flap-fold {
    position: absolute;
    top: 0;
    left: 0;
  }
  .watermark-mark {
    position: absolute;
    left: 610px;
    top: 770px;
    width: 300px;
    height: 300px;
    border-radius: 50%;
    border: 14px solid var(--watermark);
    box-sizing: border-box;
  }
  .brand {
    position: absolute;
    left: 40px;
    top: 930px;
  }
  .brand-dot {
    width: 96px;
    height: 96px;
    border-radius: 50%;
    background: var(--brand-blue);
    margin-left: 8px;
  }
  .brand-name {
    margin: 26px 0 0;
    font-size: 25px;
    font-weight: 500;
    letter-spacing: 0.02em;
    color: var(--ink);
    white-space: nowrap;
  }
  .address {
    position: absolute;
    left: 426px;
    top: 948px;
    font-size: 14px;
    line-height: 1.75;
    color: var(--ink);
    font-style: normal;
  }
  .address p { margin: 0; white-space: nowrap; }
  .band {
    position: absolute;
    left: 0;
    right: 0;
    top: 1098px;
    height: 26px;
    background: linear-gradient(90deg, var(--band-light) 0%, var(--brand-blue) 55%, var(--brand-navy) 100%);
  }
</style>
</head>
<body>
  <div class="envelope">
    <svg class="flap-fold" width="849" height="140" viewBox="0 0 849 140" aria-hidden="true">
      <path d="M0 6 Q20 108 120 108 L729 108 Q829 108 849 6" fill="none" stroke="var(--fold-line)" stroke-width="2"/>
    </svg>

    <div class="watermark-mark" aria-hidden="true"></div>

    <div class="brand">
      <div class="brand-dot" aria-hidden="true"></div>
      <p class="brand-name">青葉台相続専門税理士事務所</p>
    </div>

    <address class="address">
      <p>〒150-0012</p>
      <p>東京都架空区青葉台2-4-1 青葉台テラス403</p>
      <p>TEL. 03-0000-4821</p>
    </address>

    <div class="band"></div>
  </div>
</body>
</html>
```